Letterhead and Envelopes design using existing logo. Logo can be found at tqvanholt.com

Use existing logo (attached) and incorporate in letterhead and envelope designs.

Current logo can be viewed at tqvanholt.com the web site reflect various parent and sub companies. Please see attached as well.

Target Market(s)

Other oil and gas operators.

Industry/Entity Type

Oil And Gas

Font styles to use
Sans Serif

Colors

Designer to choose colors to be used in the design.

Requirements
Must have
• Current logo and address
Nice to have
• Modern, contemporary approach yet incorporate existing traditional design.
• After design is selected for Wexford Tiller Holdings I will use similar design for Royalties, Exploration, Energy and Farms with different color schemes.

```html
<!DOCTYPE html>
<html lang="en">
<head>
<meta charset="utf-8">
<title>Wexford Tiller Holdings — Stationery</title>
<link rel="stylesheet" href="https://fonts.googleapis.com/css2?family=Roboto:wght@400;500;700&display=swap">
<style>
  :root {
    --backdrop: #4f5255;
    --paper: #f1f1f1;
    --ink: #3a3a3a;
    --ink-soft: #6b6b6b;
    --brand-green: #4a8a2a;
    --brand-dark: #1f1f1f;
    --signature-tint: #e3e6ec;
    --flap-text: #e6efe0;
  }
  * { box-sizing: border-box; margin: 0; padding: 0; }
  html, body { width: 1200px; height: 749px; overflow: hidden; }
  body {
    background: var(--backdrop);
    font-family: "Roboto", Arial, sans-serif;
    color: var(--ink);
    position: relative;
  }
  .sheet { position: absolute; background: var(--paper); overflow: hidden; }

  /* Brand lockup */
  .brand-lockup { position: absolute; display: flex; align-items: center; gap: 6px; }
  .brand-lockup .brand-dot {
    width: 14px; height: 14px; border-radius: 50%; background: var(--brand-green); flex: none;
  }
  .brand-lockup .brand-name {
    font-weight: 700; font-size: 9px; line-height: 1.15; color: var(--brand-dark); width: 70px;
  }

  /* Letterhead */
  .letterhead { left: 171px; top: 111px; width: 373px; height: 526px; }
  .letterhead .brand-lockup { left: 23px; top: 40px; }
  .letter-date, .recipient, .salutation, .letter-body, .sign-off {
    position: absolute; left: 23px; font-size: 5.8px; color: var(--ink-soft);
  }
  .letter-date { top: 129px; }
  .recipient { top: 154px; line-height: 8.4px; }
  .recipient strong { color: var(--ink); font-weight: 700; }
  .salutation { top: 205px; }
  .letter-body { top: 221px; width: 326px; line-height: 8.4px; text-align: justify; }
  .letter-body p + p { margin-top: 8.4px; }
  .sign-off { top: 414px; }
  .sign-off .signer-name { font-weight: 700; color: var(--ink); }
  .signature-area {
    display: block; width: 84px; height: 14px; margin: 8px 0 1px -8px;
    background: var(--signature-tint); border-radius: 2px;
  }
  .company-block {
    position: absolute; right: 24px; top: 455px; text-align: right;
  }
  .company-block .company-name {
    font-size: 8.6px; font-weight: 700; color: var(--brand-green); margin-bottom: 5px;
  }
  .contact-line {
    font-size: 5.4px; line-height: 7.4px; color: var(--ink);
    display: flex; justify-content: flex-end; align-items: center; gap: 3px;
  }
  .contact-line svg { width: 5px; height: 5px; fill: var(--brand-green); }

  /* Envelope front */
  .envelope-front { left: 578px; top: 162px; width: 450px; height: 202px; }
  .envelope-front .brand-lockup { left: 26px; top: 38px; }
  .return-address {
    position: absolute; right: 31px; top: 177px; font-size: 7.6px; font-weight: 400; color: var(--brand-dark);
  }

  /* Envelope back */
  .envelope-back { left: 578px; top: 386px; width: 450px; height: 202px; }
  .envelope-flap { position: absolute; left: 0; top: 0; }
  .flap-web {
    position: absolute; left: 0; width: 100%; top: 33px; text-align: center;
    font-size: 5.4px; letter-spacing: 1.2px; color: var(--flap-text);
  }
</style>
</head>
<body>

  <section class="sheet letterhead" aria-label="Letterhead">
    <div class="brand-lockup">
      <span class="brand-dot"></span>
      <span class="brand-name">Wexford Tiller Holdings</span>
    </div>

    <div class="letter-date">30/20/2016</div>
    <div class="recipient">
      <strong>Mr. XYZ Smith</strong><br>
      123, Street No. 123,<br>
      City Name<br>
      Pincode-123456
    </div>
    <div class="salutation">Dear Sir,</div>

    <div class="letter-body">
      <p>Lorem Ipsum is simply dummy text of the printing and typesetting industry. Lorem Ipsum has been the industry's standard dummy text ever since the 1500s, when an unknown printer took a galley of type and scrambled it to make a type specimen book. It has survived not only five centuries, but also the leap into electronic typesetting, remaining essentially unchanged. It was popularised in the 1960s with the release of Glyphwell sheets containing Lorem Ipsum passages, and more recently with desktop publishing software like Quillmark Layout including versions of Lorem Ipsum.</p>
      <p>Lorem Ipsum is simply dummy text of the printing and typesetting industry. Lorem Ipsum has been the industry's standard dummy text ever since the 1500s, when an unknown printer took a galley of type and scrambled it to make a type specimen book. It has survived not only five centuries, but also the leap into electronic typesetting, remaining essentially unchanged. It was popularised in the 1960s with the release of Glyphwell sheets containing Lorem Ipsum passages, and more recently with desktop publishing software like Quillmark Layout including versions of Lorem Ipsum.</p>
      <p>Lorem Ipsum is simply dummy text of the printing and typesetting industry. Lorem Ipsum has been the industry's standard dummy text ever since the 1500s, when an unknown printer took a galley of type and scrambled it to make a type specimen book.</p>
      <p>Lorem Ipsum is simply dummy text of the printing and typesetting industry. Lorem Ipsum has been the industry's standard dummy text ever since the 1500s, when an unknown printer took a galley of type and scrambled it to make a type specimen book.</p>
    </div>

    <div class="sign-off">
      <div class="signer-name">Your Name</div>
      <span class="signature-area" role="img" aria-label="Handwritten signature"></span>
      <div>CEO &nbsp;|&nbsp; Owner</div>
    </div>

    <div class="company-block">
      <div class="company-name">Wexford Tiller Holdings, LLC</div>
      <div class="contact-line">(555) 014.2280
        <svg viewBox="0 0 10 10"><path d="M2 0.5l2 2-1 1.5c.6 1.3 1.6 2.3 2.9 2.9l1.5-1 2 2-1.4 1.6C4.5 9.5.5 5.5.4 1.9z"/></svg>
      </div>
      <div class="contact-line">www.tqvanholt.com
        <svg viewBox="0 0 10 10"><circle cx="5" cy="5" r="4.5"/></svg>
      </div>
      <div class="contact-line">reception@tqvanholt.com
        <svg viewBox="0 0 10 10"><path d="M0 2h10v6H0z"/></svg>
      </div>
      <div class="contact-line">PO Box 318 Harlow Springs, Montana 59210</div>
    </div>
  </section>

  <section class="sheet envelope-front" aria-label="Envelope front">
    <div class="brand-lockup">
      <span class="brand-dot"></span>
      <span class="brand-name">Wexford Tiller Holdings</span>
    </div>
    <div class="return-address">PO Box 318 Harlow Springs, Montana 59210</div>
  </section>

  <section class="sheet envelope-back" aria-label="Envelope back">
    <svg class="envelope-flap" width="450" height="72" viewBox="0 0 450 72">
      <path d="M0 0H450L420 56Q412 72 392 72H58Q38 72 30 56Z" fill="var(--brand-green)"/>
    </svg>
    <div class="flap-web">www.tqvanholt.com</div>
  </section>

</body>
</html>
```